Zielgruppe
Wir sind ein kleiner familiengeführter Weinbaubetrieb am Wagram und suchen einen modernen und naturnahen Namen und ein Etikett mit Blickfang für unseren Wermut, aus handgepflückten regionalen Wildkräutern mit Rosewein vom Zweigelt. Charakeristik des Getränks: Aperitif, Zitrusnote, leichte Bitternote, mit Tonic water als Cocktail.
Unsere Zielgruppe: kaufkräftige Genussmenschen im mittleren Alter
Aufgabenstellung
Etikett für 0,5l Flasche, Flasche noch nicht festgelegt, Etikettenhöhe: 65mm
Was soll draufstehen: Name, Vermouth, local botanicals, handcrafted, small batch

```html
<!DOCTYPE html>
<html lang="en">
<head>
<meta charset="UTF-8">
<title>Vermouth Rosé – Label</title>
<link rel="stylesheet" href="https://fonts.googleapis.com/css2?family=Marcellus&family=Open+Sans:wght@400;500&display=swap">
<style>
  :root {
    --canvas: #ffffff;
    --label-orange: #c75a1e;
    --frame-blue: #3d6f98;
    --title-coral: #e24f4e;
    --ink-navy: #3b3c8c;
    --rule-blue: #5a86b0;
    --accent-pink: #d96a86;
  }
  * { margin: 0; padding: 0; box-sizing: border-box; }
  html, body {
    width: 1200px; height: 1200px; overflow: hidden;
    background: var(--canvas);
  }
  .canvas { position: relative; width: 1200px; height: 1200px; }

  .label {
    position: absolute;
    left: 303px; top: 62px;
    width: 594px; height: 1076px;
    background: var(--label-orange);
    border: 11px solid var(--frame-blue);
  }

  .label-title {
    position: absolute;
    left: 60px; top: 50px;
    width: 80px; height: 640px;
    writing-mode: vertical-rl;
    font-family: "Marcellus", serif;
    font-size: 86px;
    line-height: 80px;
    letter-spacing: 6px;
    color: var(--title-coral);
  }

  .label-hatch {
    position: absolute;
    left: 350px; top: 430px;
    width: 210px; height: 250px;
    background: linear-gradient(135deg, rgba(232,110,60,0) 30%, rgba(232,110,60,0.55) 60%, rgba(232,110,60,0) 90%);
  }

  .label-variety {
    position: absolute;
    left: 58px; top: 728px;
    font-family: "Marcellus", serif;
    font-size: 30px;
    letter-spacing: 2px;
    color: var(--ink-navy);
  }

  .rule {
    position: absolute;
    left: 58px; width: 456px; height: 2px;
    background: var(--rule-blue);
  }
  .rule--top { top: 762px; }
  .rule--bottom { top: 830px; }

  .label-claims {
    position: absolute;
    left: 58px; top: 774px;
    font-family: "Open Sans", sans-serif;
    font-size: 33px;
    line-height: 48px;
    color: var(--ink-navy);
    white-space: nowrap;
  }

  .label-batch {
    position: absolute;
    left: 68px; top: 842px;
    font-family: "Open Sans", sans-serif;
    font-size: 22px;
    color: var(--accent-pink);
  }

  .label-grapes {
    position: absolute;
    left: 78px; top: 880px;
    width: 105px; height: 125px;
    border-radius: 50% 50% 50% 50% / 40% 40% 60% 60%;
    background: radial-gradient(circle at 50% 40%, rgba(110,70,170,0.55), rgba(110,70,170,0.15) 70%);
  }

  .divider {
    position: absolute;
    left: 232px; top: 856px;
    width: 2px; height: 180px;
    background: var(--ink-navy);
  }

  .label-specs {
    position: absolute;
    left: 270px; top: 860px;
    font-family: "Open Sans", sans-serif;
    color: var(--ink-navy);
    letter-spacing: 5px;
  }
  .spec { display: block; font-size: 50px; line-height: 74px; }
  .spec-unit { font-size: 26px; letter-spacing: 2px; }
</style>
</head>
<body>
<main class="canvas">
  <section class="label">
    <h1 class="label-title">VERMOUTH</h1>
    <div class="label-hatch" role="img" aria-label="Decorative diagonal line texture"></div>
    <p class="label-variety">ROSE</p>
    <div class="rule rule--top"></div>
    <p class="label-claims">local botanicals | handcrafted</p>
    <div class="rule rule--bottom"></div>
    <p class="label-batch">small batch</p>
    <div class="label-grapes" role="img" aria-label="Outline illustration of a grape cluster"></div>
    <div class="divider"></div>
    <p class="label-specs">
      <span class="spec">17%<span class="spec-unit">vol</span></span>
      <span class="spec">500ml</span>
    </p>
  </section>
</main>
</body>
</html>
```